Altamira Business Card Design

The name of the business is Ruben Altamira, CPA LLC
The service that we offer is Accounting, Tax & Consulting Services. I need it to have the following items:
Ruben Altamira, Principal
Phone Number
Email Address
Physical Address

I have attached the company logo, one in black and one in white. Please provide a design in black background and the other in white background. Please include "Accounting, Tax & Consulting Services". I want the business card to be clean and very professional.

```html
<!DOCTYPE html>
<html lang="en">
<head>
<meta charset="utf-8">
<title>Ruben Altamira, CPA LLC – Business Card</title>
<link href="https://fonts.googleapis.com/css2?family=Montserrat:wght@400;600;700&family=Open+Sans:wght@400&display=swap" rel="stylesheet">
<style>
  :root {
    --backdrop: #d9d9d9;
    --card-black: #1f1f20;
    --card-white: #ffffff;
    --silver: #c9c9cb;
    --silver-dim: #9a9a9c;
    --brand-red: #a0151b;
    --ink: #3a3a3a;
    --rule: #555555;
  }
  * { margin: 0; padding: 0; box-sizing: border-box; }
  html, body { width: 1200px; height: 900px; overflow: hidden; }
  body {
    background: var(--backdrop);
    display: flex;
    flex-direction: column;
    align-items: center;
    justify-content: center;
    gap: 60px;
  }
  .card {
    width: 600px;
    height: 343px;
    position: relative;
    box-shadow: 0 6px 18px rgba(0,0,0,0.18);
  }

  /* Front: black */
  .card-front {
    background: var(--card-black);
    display: flex;
    flex-direction: column;
    align-items: center;
    justify-content: center;
  }
  .brand-square {
    width: 54px;
    height: 54px;
    background: var(--silver-dim);
    margin-bottom: 22px;
  }
  .brand-name {
    font-family: "Montserrat", sans-serif;
    font-weight: 600;
    font-size: 26px;
    color: var(--silver);
    letter-spacing: 0.5px;
  }
  .brand-title {
    font-family: "Montserrat", sans-serif;
    font-weight: 600;
    font-size: 13px;
    color: var(--silver);
    letter-spacing: 3.4px;
    margin-top: 6px;
  }

  /* Back: white */
  .card-back { background: var(--card-white); }
  .identity {
    position: absolute;
    right: 270px;
    top: 128px;
    text-align: right;
  }
  .person-name {
    font-family: "Montserrat", sans-serif;
    font-weight: 700;
    font-size: 24px;
    color: var(--brand-red);
    letter-spacing: 0.3px;
  }
  .person-role {
    font-family: "Open Sans", sans-serif;
    font-size: 14px;
    color: var(--ink);
    margin-top: 2px;
  }
  .divider {
    position: absolute;
    left: 350px;
    top: 100px;
    width: 1px;
    height: 106px;
    background: var(--rule);
  }
  .contact {
    position: absolute;
    left: 368px;
    top: 98px;
    font-family: "Open Sans", sans-serif;
    font-size: 13px;
    color: var(--ink);
    line-height: 18px;
  }
  .address { margin-bottom: 10px; }
  .contact-line { display: flex; align-items: center; gap: 8px; }
  .contact-line svg { width: 10px; height: 10px; fill: var(--brand-red); flex: none; }
  .service-band {
    position: absolute;
    left: 0;
    right: 0;
    top: 250px;
    height: 30px;
    background: var(--brand-red);
    display: flex;
    align-items: center;
    justify-content: center;
  }
  .service-line {
    font-family: "Montserrat", sans-serif;
    font-weight: 600;
    font-size: 13px;
    color: var(--card-white);
    letter-spacing: 3.6px;
  }
</style>
</head>
<body>
  <section class="card card-front">
    <div class="brand-square"></div>
    <div class="brand-name">RUBEN ALTAMIRA, CPA, LLC</div>
    <div class="brand-title">CERTIFIED PUBLIC ACCOUNTANT</div>
  </section>

  <section class="card card-back">
    <div class="identity">
      <div class="person-name">RUBEN ALTAMIRA</div>
      <div class="person-role">Principal</div>
    </div>
    <div class="divider"></div>
    <div class="contact">
      <div class="address">1420 Birchwood Court<br>Anchorage, Alaska 34512</div>
      <div class="contact-line">
        <svg viewBox="0 0 10 10"><path d="M2 0.5 L3.6 2.6 L2.7 3.6 Q3.8 5.9 6.4 7.3 L7.4 6.4 L9.5 8 L8.4 9.5 Q4.5 9.3 1.6 5.8 Q0.4 3.8 0.6 1.6 Z"/></svg>
        <span>369-555-0142</span>
      </div>
      <div class="contact-line">
        <svg viewBox="0 0 10 10"><path d="M0 2 H10 V8.5 H0 Z M0.8 2.6 L5 5.6 L9.2 2.6 V3.4 L5 6.4 L0.8 3.4 Z" fill-rule="evenodd"/></svg>
        <span>name@rubenaltamiracpa.com</span>
      </div>
      <div class="contact-line">
        <svg viewBox="0 0 10 10"><circle cx="5" cy="5" r="4.8"/></svg>
        <span>rubenaltamiracpa.com</span>
      </div>
    </div>
    <div class="service-band">
      <span class="service-line">ACCOUNTING, TAX &amp; CONSULTING SERVICES</span>
    </div>
  </section>
</body>
</html>
```